Business Card Design for an international medical business

We need a professional and elegant business card design with fashionable graphic element. Our company is located in Hong Kong with three worldwide production lines for medical equipment(surgical face masks, N95, face shields and so on). Our factories all contain medical standard ISOs and all product fulfill Garrow lab and KTR testing standards.

We would like to see designs that show the impression of our professional expertise, formal corporate image with creative thinking work style and inspiring global concept. We want the content in both English and Japanese on the same card. We also want to print our the patent trade mark and company logo on the card.

Target Market(s)

Southeast Asia, US, EU

Industry/Entity Type

Medical Equipment

Contact Information for Business Card

Below are the content we want to be shown on the business card(please help us to simplified them to be more presentable and readable):

Company name: Brightmoor (Hong Kong) 5K Medical Technology Company Limited
Address: Unit 2204, 22/F, Pine Court, No.8 Ferndale Road, Kwun Lam, Hong Kong.
Band Name: B5K
Homepage: www.brightmoor5kq.com
Name: Lok Wing Fei
Title: Manager
Tel: +852-xxxx-xxxx
Mobile: +852-xxxx-xxxx
Email: xx@brightmoor5kq.com

Production Lines:
China: Ping Shan Kai Lok Medical Technology Company Limited
Mo Tan City Ren Bo Textile Machinery Company Limited
Bangladesh: B5K Medical Technology Company Limited

Qualifications:
ISO 13485:2016
ISO 14644-1:2015
ISO Class 8 Cleanroom
ASTM F2100 Level 2
EN14683 Type IIR
EN149 FFP2
CE Certified
FDA Registration number: XXX

Requirements
Must have
• use pantone color for the design
and provide the pantone number for printing purpose
Should not have
• Background color should not be black.

```html
<!DOCTYPE html>
<html lang="en">
<head>
<meta charset="utf-8">
<title>B5K Business Card</title>
<link rel="stylesheet" href="https://fonts.googleapis.com/css2?family=Roboto:wght@400;700&display=swap">
<style>
  :root {
    --backdrop: #b9b9b9;
    --card: #ffffff;
    --pink: #ef0a52;
    --teal: #1bb8b8;
    --mauve: #7a6a8f;
    --ink: #1e1e1e;
  }
  html, body {
    margin: 0;
    padding: 0;
    width: 1200px;
    height: 801px;
    overflow: hidden;
    background: var(--backdrop);
    font-family: "Roboto", Arial, sans-serif;
  }
  .stage { position: relative; width: 1200px; height: 801px; }
  .card {
    position: absolute;
    top: 274px;
    width: 443px;
    height: 263px;
    background: var(--card);
    overflow: hidden;
  }
  .card--front { left: 153px; background: linear-gradient(30deg, var(--pink) 0%, #b8366e 30%, var(--mauve) 55%, var(--teal) 88%); }
  .card--back { left: 625px; }

  .front-blank { position: absolute; inset: 0; }

  .brand-front {
    position: absolute; left: 24px; top: 24px;
    font-weight: 700; font-size: 36px; line-height: 1;
    color: #fff; letter-spacing: 2px;
    display: flex; align-items: center; gap: 10px;
  }
  .brand-front .dot { width: 14px; height: 14px; border-radius: 50%; background: #fff; }

  .person { position: absolute; left: 26px; top: 85px; color: #fff; }
  .person__name { font-weight: 700; font-size: 17px; letter-spacing: -0.3px; line-height: 1.1; }
  .person__title { font-size: 13px; line-height: 1.1; }

  .contacts { position: absolute; left: 26px; top: 125px; margin: 0; padding: 0; list-style: none; color: #fff; font-size: 12.5px; }
  .contacts li { display: flex; align-items: center; gap: 4px; height: 15.6px; }
  .contacts svg { width: 11px; height: 11px; flex: none; }

  .address { position: absolute; left: 27px; top: 196px; color: #fff; font-size: 12.5px; line-height: 15.6px; margin: 0; font-style: normal; }

  .brand-back {
    position: absolute; left: 0; right: 0; top: 36px;
    display: flex; justify-content: center; align-items: center; gap: 10px;
  }
  .brand-back .dot { width: 16px; height: 16px; border-radius: 50%; background: var(--pink); }
  .brand-back .word { font-weight: 700; font-size: 34px; color: var(--pink); letter-spacing: 1px; line-height: 1; }

  .info { position: absolute; left: 0; right: 0; text-align: center; color: var(--ink); font-size: 13px; line-height: 15.6px; white-space: nowrap; }
  .info--lines { top: 100px; }
  .info--quals { top: 183px; }
  .info__heading { color: var(--pink); font-weight: 700; font-size: 13.5px; }
  .label { color: var(--teal); font-weight: 700; }
  .sep { color: var(--teal); }
  .divider { position: absolute; left: 152px; width: 139px; top: 173px; height: 1px; background: var(--teal); }
</style>
</head>
<body>
<div class="stage">
  <section class="card card--front">
    <svg class="front-blank" viewBox="0 0 443 263" aria-hidden="true">
      <path d="M318 0 C250 60 205 150 240 205 L300 263 L443 263 L443 0 Z" fill="#ffffff"/>
    </svg>
    <div class="brand-front"><span class="dot"></span>B5K</div>
    <div class="person">
      <div class="person__name">LOK WING FEI</div>
      <div class="person__title">Manager</div>
    </div>
    <ul class="contacts">
      <li><svg viewBox="0 0 24 24"><path fill="#fff" d="M6.6 10.8a15.1 15.1 0 0 0 6.6 6.6l2.2-2.2c.3-.3.7-.4 1-.2 1.1.4 2.3.6 3.6.6.6 0 1 .4 1 1V20c0 .6-.4 1-1 1C10.6 21 3 13.4 3 4c0-.6.4-1 1-1h3.5c.6 0 1 .4 1 1 0 1.3.2 2.5.6 3.6.1.3 0 .7-.2 1z"/></svg>+852-xxxx-xxxx</li>
      <li><svg viewBox="0 0 24 24"><rect x="6" y="2" width="12" height="20" rx="2" fill="none" stroke="#fff" stroke-width="2.4"/><circle cx="12" cy="18" r="1.3" fill="#fff"/></svg>+852-xxxx-xxxx</li>
      <li><svg viewBox="0 0 24 24"><rect x="2" y="5" width="20" height="14" fill="none" stroke="#fff" stroke-width="2"/><path d="M2 5l10 8 10-8" fill="none" stroke="#fff" stroke-width="2"/></svg>xx@brightmoor5kq.com</li>
      <li><svg viewBox="0 0 24 24"><g fill="none" stroke="#fff" stroke-width="1.8"><circle cx="12" cy="12" r="10"/><ellipse cx="12" cy="12" rx="4.5" ry="10"/><path d="M2 12h20M4 7h16M4 17h16"/></g></svg>www.brightmoor5kq.com</li>
    </ul>
    <address class="address">Unit 2204, 22/F, Pine Court<br>No.8 Ferndale Road<br>Kwun Lam, Hong Kong.</address>
  </section>

  <section class="card card--back">
    <div class="brand-back"><span class="dot"></span><span class="word">BRIGHTMOOR</span></div>
    <div class="info info--lines">
      <div class="info__heading">PRODUCTION LINES</div>
      <div><span class="label">CHINA:</span> Ping Shan Kai Lok Medical Technology Company Limited</div>
      <div>Mo Tan City Ren Bo Textile Machinery Company Limited</div>
      <div><span class="label">BANGLADESH:</span> B5K Medical Technology Company Limited</div>
    </div>
    <div class="divider"></div>
    <div class="info info--quals">
      <div class="info__heading">QUALIFICATIONS</div>
      <div>ISO 13485:2016 <span class="sep">|</span> ISO 14644-1:2015 <span class="sep">|</span> ISO Class 8 Cleanroom</div>
      <div>ASTM F2100 Level 2 <span class="sep">|</span> EN14683 Type IIR <span class="sep">|</span> EN149 FFP2</div>
      <div>CE Certified <span class="sep">|</span> FDA Registration number: XXX</div>
    </div>
  </section>
</div>
</body>
</html>
```